KOVA WIRING PTE LTD
KOVA WIRING NAME CARD
Project: KOVA WIRING PTE LTD
KOVA WIRING PTE LTD - Engineering
Creative Brief
Professional
Deren Whitcombe
Manager
57 Tannery Lane #03-22 Silverbrook Industrial Complex Singapore 347912
derenkovawiring@mailbox-example.net
Reg No. 198733502K
https://www.filevault-example.net/share/7qe2kx9/ZTRmPwq4HnLc?dl=0 Pleas find folder for the logo design A.I. file. Thanks Client love the 3 colour in the logo design for FengShui purposes.
harlowbek harlowbek
Hi my client like your design #218, Can you give the stationary set for #218. We try to finalize by tomorrow. Thanks

```html
<!DOCTYPE html>
<html lang="en">
<head>
<meta charset="utf-8">
<title>KOVA WIRING – Name Card</title>
<link href="https://fonts.googleapis.com/css2?family=Roboto:wght@400;500;700&display=swap" rel="stylesheet">
<style>
  :root {
    --stage: #d9d9d6;
    --card-white: #ffffff;
    --card-black: #0b0b0c;
    --ink: #1d1d1f;
    --ink-soft: #4a4a4f;
    --green: #138a45;
    --green-bright: #22a455;
    --blue: #1d2a8c;
    --violet: #4b2a8a;
    --grey-edge: #b9bcc0;
  }
  * { margin: 0; padding: 0; box-sizing: border-box; }
  html, body { width: 1200px; height: 904px; overflow: hidden; }
  body {
    background: var(--stage);
    font-family: "Roboto", Arial, sans-serif;
    position: relative;
  }
  .card {
    position: absolute;
    width: 700px;
    height: 400px;
    left: 250px;
    box-shadow: 0 6px 18px rgba(0,0,0,0.22);
    overflow: hidden;
  }
  .card-back { top: 32px; background: var(--card-black); }
  .card-front { top: 472px; background: var(--card-white); }

  /* back */
  .back-brand {
    position: absolute; left: 50%; top: 50%;
    transform: translate(-50%, -50%);
    display: flex; align-items: center; gap: 14px;
  }
  .brand-square { width: 34px; height: 34px; background: var(--green); }
  .back-brand .brand-name {
    color: #ffffff; font-weight: 700; font-size: 26px; letter-spacing: 3px;
  }

  /* front */
  .stripes { position: absolute; left: 0; top: 0; width: 140px; height: 400px; }
  .front-brand {
    position: absolute; left: 58px; top: 122px;
    display: flex; align-items: center; gap: 12px;
  }
  .brand-circle { width: 52px; height: 52px; border-radius: 50%; background: var(--card-black); border: 4px solid #fff; }
  .front-brand .brand-name {
    color: var(--ink); font-weight: 700; font-size: 30px; letter-spacing: 2px;
  }
  .address {
    position: absolute; left: 158px; top: 196px;
    font-size: 12.5px; line-height: 17px; color: var(--ink-soft);
  }
  .contacts {
    position: absolute; left: 132px; top: 272px;
    list-style: none; font-size: 12.5px; line-height: 17px; color: var(--ink-soft);
  }
  .contacts li { display: flex; align-items: center; gap: 10px; }
  .contacts svg { width: 12px; height: 12px; fill: var(--green); flex: none; }
  .person {
    position: absolute; right: 70px; top: 96px; text-align: right;
  }
  .person-name { color: var(--green-bright); font-weight: 500; font-size: 17px; }
  .person-role { color: var(--ink-soft); font-size: 12px; margin-top: 3px; }
</style>
</head>
<body>
  <section class="card card-back" aria-label="Card back">
    <div class="back-brand">
      <span class="brand-square"></span>
      <span class="brand-name">KOVA WIRING</span>
    </div>
  </section>

  <section class="card card-front" aria-label="Card front">
    <svg class="stripes" viewBox="0 0 140 400" aria-hidden="true">
      <defs>
        <linearGradient id="blueBand" x1="0" y1="0" x2="0" y2="1">
          <stop offset="0" stop-color="#2b3aa8"/>
          <stop offset="1" stop-color="#3a1f78"/>
        </linearGradient>
      </defs>
      <rect x="0" y="0" width="12" height="400" fill="#b9bcc0"/>
      <rect x="12" y="0" width="38" height="400" fill="#138a45"/>
      <rect x="50" y="0" width="24" height="400" fill="#0b0b0c"/>
      <rect x="74" y="0" width="40" height="400" fill="url(#blueBand)"/>
      <rect x="114" y="0" width="8" height="400" fill="#138a45"/>
      <rect x="0" y="108" width="140" height="78" fill="#ffffff"/>
    </svg>

    <div class="front-brand">
      <span class="brand-circle"></span>
      <span class="brand-name">KOVA WIRING</span>
    </div>

    <p class="address">
      57 Tannery Lane<br>
      #03-22 Silverbrook Industrial Complex<br>
      Singapore 347912
    </p>

    <ul class="contacts">
      <li><svg viewBox="0 0 12 12"><path d="M2 1h3l1 3-1.5 1a7 7 0 0 0 2.5 2.5L8 6l3 1v3a1 1 0 0 1-1 1A9 9 0 0 1 1 2a1 1 0 0 1 1-1z"/></svg>(65) 62104418</li>
      <li><svg viewBox="0 0 12 12"><path d="M3 0h6a1 1 0 0 1 1 1v10a1 1 0 0 1-1 1H3a1 1 0 0 1-1-1V1a1 1 0 0 1 1-1zm0 2v7h6V2z"/></svg>(65) 91357720</li>
      <li><svg viewBox="0 0 12 12"><path d="M3 0h6v3H3zM1 4h10v6H9V8H3v2H1zm2 5h6v3H3z"/></svg>(65) 62104419</li>
      <li><svg viewBox="0 0 12 12"><path d="M0 2h12v8H0zm1 1v.4l5 3.3 5-3.3V3z"/></svg>derenkovawiring@mailbox-example.net</li>
    </ul>

    <div class="person">
      <div class="person-name">Deren Whitcombe</div>
      <div class="person-role">Manager</div>
    </div>
  </section>
</body>
</html>
```